Documentary Movie Needs a Poster

We need a poster/lobby card for a documentary film made by six filmmakers. Lobby card needs to list name of sponsor, names of filmmakers and (if feasible, but not required) image frames from each of the six sections of the film.

Text should be very readable. OK to have all caps text or upper/lower.

Design comps are OK, these do not need to be print-ready final images.

Target Market(s)

well educated documentary filmgoers

Industry/Entity Type

Movie

Requirements
Must have
• Must contain the following text (please use helvetica neue or similar font).

Please use the following sponsor name:

The
Marlowe Institute for Cinema
presents

Please use the following filmmaker names:

Theodore Pelusky
Robert Nash
Frederick Tamworth
Harold E. F. Pratt
Vincent Lorimer
Danny Frost

Please use the 6 images in archive/zip to create the card.

You can also do text-only versions of the card (no images).

Card needs to be 2:1 aspect ratio (2000px wide x 1000 pixels high)

Names of filmmakers should each be same size (no filmmaker has visual priority over the other).

Colors for text, lines and other design elements should be RED, BLACK and/or WHITE.

Feel free to crop images if you need to.

```html
<!DOCTYPE html>
<html lang="en">
<head>
<meta charset="utf-8">
<title>Marlowe Institute for Cinema presents</title>
<link rel="stylesheet" href="https://fonts.googleapis.com/css2?family=Poiret+One&family=PT+Sans:wght@400;700&display=swap">
<style>
  :root {
    --sage-light: #d8dbc6;
    --sage-mid: #bdbf9f;
    --olive: #a9ac86;
    --olive-deep: #2f3125;
    --title-red: #8e1820;
    --white: #ffffff;
    --shadow: rgba(40, 42, 28, 0.55);
  }
  html, body {
    margin: 0;
    padding: 0;
    overflow: hidden;
    background: var(--olive-deep);
  }
  .card {
    position: relative;
    width: 1200px;
    height: 848px;
    overflow: hidden;
    font-family: "PT Sans", "Helvetica Neue", Arial, sans-serif;
  }
  .card__backdrop {
    position: absolute;
    inset: 0;
    width: 1200px;
    height: 848px;
  }
  .sponsor {
    position: absolute;
    left: 0;
    top: 0;
    width: 1200px;
    margin: 0;
    text-align: center;
  }
  .sponsor__lead,
  .sponsor__tail {
    position: absolute;
    color: var(--white);
    font-weight: 700;
    text-shadow: 0 2px 6px var(--shadow);
    line-height: 1;
  }
  .sponsor__lead {
    left: 478px;
    top: 124px;
    font-size: 52px;
  }
  .sponsor__tail {
    left: 0;
    width: 1206px;
    top: 352px;
    font-size: 64px;
    font-weight: 400;
    letter-spacing: 1px;
  }
  .sponsor__name {
    position: absolute;
    left: 0;
    width: 1200px;
    color: var(--title-red);
    font-family: "Poiret One", "Helvetica Neue", sans-serif;
    font-weight: 400;
    font-size: 104px;
    line-height: 1;
    text-shadow: 0 1px 2px rgba(255,255,255,0.25);
    white-space: nowrap;
  }
  .sponsor__name--first { top: 170px; letter-spacing: 1px; }
  .sponsor__name--second { top: 262px; letter-spacing: 1px; }
  .divider {
    position: absolute;
    left: 220px;
    top: 439px;
    width: 760px;
    height: 2px;
    background: linear-gradient(90deg, rgba(255,255,255,0) 0%, rgba(255,255,255,0.95) 40%, rgba(255,255,255,0.95) 60%, rgba(255,255,255,0) 100%);
  }
  .filmmakers {
    position: absolute;
    left: 0;
    top: 474px;
    width: 1234px;
    margin: 0;
    padding: 0;
    list-style: none;
    text-align: center;
  }
  .filmmakers__name {
    color: var(--white);
    font-size: 31px;
    font-weight: 700;
    line-height: 43.5px;
    letter-spacing: 1px;
    text-shadow: 0 1px 4px var(--shadow);
  }
</style>
</head>
<body>
  <main class="card">
    <svg class="card__backdrop" viewBox="0 0 1200 848" aria-hidden="true">
      <defs>
        <linearGradient id="lowerField" x1="0" y1="0" x2="0" y2="1">
          <stop offset="0" stop-color="#b3b590"/>
          <stop offset="0.55" stop-color="#a5a882"/>
          <stop offset="0.82" stop-color="#7c7f60"/>
          <stop offset="1" stop-color="#2c2e22"/>
        </linearGradient>
        <linearGradient id="upperField" x1="0" y1="0" x2="1" y2="1">
          <stop offset="0" stop-color="#dfe1cf"/>
          <stop offset="1" stop-color="#cfd2b9"/>
        </linearGradient>
        <radialGradient id="edgeShade" cx="0.5" cy="0.45" r="0.75">
          <stop offset="0.6" stop-color="#000" stop-opacity="0"/>
          <stop offset="1" stop-color="#000" stop-opacity="0.18"/>
        </radialGradient>
      </defs>
      <rect width="1200" height="848" fill="url(#lowerField)"/>
      <polygon points="0,0 1200,0 1200,224 0,410" fill="url(#upperField)"/>
      <rect width="1200" height="848" fill="url(#edgeShade)"/>
    </svg>

    <h1 class="sponsor">
      <span class="sponsor__lead">The</span>
      <span class="sponsor__name sponsor__name--first">Marlowe Institute</span>
      <span class="sponsor__name sponsor__name--second">for Cinema</span>
      <span class="sponsor__tail">presents</span>
    </h1>

    <div class="divider"></div>

    <ul class="filmmakers">
      <li class="filmmakers__name">Theodore Pelusky</li>
      <li class="filmmakers__name">Robert Nash</li>
      <li class="filmmakers__name">Frederick Tamworth</li>
      <li class="filmmakers__name">Harold E. F. Pratt</li>
      <li class="filmmakers__name">Vincent Lorimer</li>
      <li class="filmmakers__name">Danny Frost</li>
    </ul>
  </main>
</body>
</html>
```